Bramblewick Dill Pickles needs your smart gourmet Design

Looking for a smart design for a dill pickle jar container. The text
Bramblewick Dill Pickles.
Simply Picklelicious.

A tasty reason to raid the refrigerator.

Target Market(s)

Foodies, farmers market types.

Font styles to use
Serif
Sans Serif

Colors

Designer to choose colors to be used in the design.

Requirements
Must have
• Attractive design to entice foodies to buy my Pickles. Not cluttered, easy to read.
Nice to have
• Pickles, garlic. Modern.
Should not have
• Clutter. No script text.

```html
<!DOCTYPE html>
<html lang="en">
<head>
<meta charset="utf-8">
<title>Bramblewick Dill Pickles – Jar Label</title>
<link href="https://fonts.googleapis.com/css2?family=Bebas+Neue&family=Cabin:ital,wght@0,400;1,700&display=swap" rel="stylesheet">
<style>
  :root {
    --backdrop: #e6e6e6;
    --label-dark: #7c2110;
    --label-mid: #b8421f;
    --label-light: #dc6734;
    --wave-red: #a3141c;
    --wave-deep: #6e0a0d;
    --ink-white: #f7f3ef;
    --pickle-green: #6f9a3a;
  }
  * { margin: 0; padding: 0; box-sizing: border-box; }
  html, body {
    width: 1200px; height: 801px; overflow: hidden;
    background: var(--backdrop);
  }
  .canvas {
    position: relative; width: 1200px; height: 801px;
    display: flex; align-items: center; justify-content: center;
  }
  .jar-label {
    position: relative; width: 780px; height: 620px; overflow: hidden;
    background: linear-gradient(90deg, var(--label-dark) 0%, var(--label-mid) 45%, var(--label-light) 100%);
  }
  .label-wave {
    position: absolute; inset: 0; width: 100%; height: 100%;
  }
  .brand-title {
    position: absolute; left: 100px; top: 70px; width: 540px;
    text-align: center; color: var(--ink-white);
    font-family: "Bebas Neue", "Oswald", sans-serif; line-height: 0.9;
  }
  .brand-name { display: block; font-size: 128px; letter-spacing: 1px; }
  .brand-product { display: block; font-size: 72px; letter-spacing: 1px; margin-top: 6px; }
  .mascot-art {
    position: absolute; left: 650px; top: 225px; width: 95px; height: 200px;
    border-radius: 40px;
    background: linear-gradient(180deg, #86b04a 0%, var(--pickle-green) 100%);
  }
  .tagline {
    position: absolute; left: 0; right: 0; top: 478px; text-align: center;
    color: var(--ink-white); font-family: "Cabin", "Helvetica Neue", sans-serif;
  }
  .tagline-main { display: block; font-size: 46px; font-weight: 400; }
  .tagline-sub { display: block; font-size: 21px; font-weight: 700; font-style: italic; margin-top: 6px; }
</style>
</head>
<body>
<main class="canvas">
  <section class="jar-label">
    <svg class="label-wave" viewBox="0 0 780 620" preserveAspectRatio="none" aria-hidden="true">
      <defs>
        <linearGradient id="waveFill" x1="0" y1="0" x2="1" y2="0">
          <stop offset="0" stop-color="#6e0a0d"/>
          <stop offset="1" stop-color="#b3171f"/>
        </linearGradient>
      </defs>
      <path d="M0 300 C 120 340, 220 460, 360 455 C 500 450, 600 380, 780 390 L 780 620 L 0 620 Z" fill="url(#waveFill)"/>
    </svg>
    <h1 class="brand-title">
      <span class="brand-name">Bramblewick</span>
      <span class="brand-product">Dill Pickles</span>
    </h1>
    <div class="mascot-art" role="img" aria-label="Cartoon illustration of two pickle characters"></div>
    <p class="tagline">
      <span class="tagline-main">Simply Picklelicious</span>
      <span class="tagline-sub">A tasty reason to raid the refrigerator.</span>
    </p>
  </section>
</main>
</body>
</html>
```